2 Business Card Designs

Need two business cards designed:
1) for lumora studio (wedding video) website is lumorastudio.com.au
2) for lumora studio (corporate video) website is lumorastudio.net.au

I am looking for something simple, no fancy shapes etc. Just elegant, simple and classy.

Both companies are video companies, one specialising in weddings the other corporate videos. Neither card needs to have any pics of video or camera related images. Please use same colour schemes as respective websites.

Logo is the same but can change colour.

Industry/Entity Type

Camera

Requirements
Must have
• Logo should be either all white or a colour to match websites
Should not have
• swirls, flowers, shapes, etc.

```html
<!DOCTYPE html>
<html lang="en">
<head>
<meta charset="utf-8">
<title>lumora studio business cards</title>
<link rel="stylesheet" href="https://fonts.googleapis.com/css2?family=Source+Sans+3:wght@400;600&family=Didact+Gothic&display=swap">
<style>
  :root {
    --backdrop: #ecd4b6;
    --label: #b46d3a;
    --card: #ffffff;
    --wedding-dark: #6b6b5c;
    --wedding-light: #dfe2c8;
    --corporate-dark: #46525d;
    --corporate-light: #b4b4b4;
    --corporate-pill: #7b7b7b;
    --ink: #141414;
    --contact-ink: #555555;
  }
  * { margin: 0; padding: 0; box-sizing: border-box; }
  html, body { width: 1200px; height: 900px; overflow: hidden; }
  body {
    position: relative;
    background: var(--backdrop);
    font-family: "Source Sans 3", Arial, sans-serif;
  }
  .set-label {
    position: absolute;
    left: 70px;
    font-size: 36px;
    color: var(--label);
    font-weight: 400;
    line-height: 1;
  }
  .set-label--wedding { top: 214px; }
  .set-label--corporate { top: 658px; }

  .card {
    position: absolute;
    left: 346px;
    width: 598px;
    height: 344px;
    background: var(--card);
    box-shadow: 0 2px 4px rgba(0,0,0,0.18);
    overflow: hidden;
  }
  .card--wedding { top: 60px; }
  .card--corporate { top: 500px; }

  .card__band { position: absolute; top: 0; left: 0; height: 100%; }
  .card--wedding .card__band--dark { width: 62px; background: var(--wedding-dark); }
  .card--wedding .card__band--light { left: 62px; width: 84px; background: var(--wedding-light); }
  .card--corporate .card__band--gradient {
    width: 146px;
    background: linear-gradient(to right, var(--corporate-dark), var(--corporate-light));
  }

  .brand {
    position: absolute;
    left: 120px;
    top: 14px;
    color: var(--ink);
    font-weight: 400;
    line-height: 1;
    text-align: center;
    width: 270px;
  }
  .brand__main { display: block; font-size: 78px; letter-spacing: 1px; }
  .brand__sub { display: block; font-size: 22px; letter-spacing: 14px; margin-top: -2px; padding-left: 60px; }

  .name-pill {
    position: absolute;
    left: 302px;
    top: 134px;
    width: 296px;
    height: 50px;
    border-radius: 25px 0 0 25px;
    font-size: 27px;
    font-weight: 600;
    line-height: 50px;
    padding-left: 38px;
    white-space: nowrap;
  }
  .card--wedding .name-pill { background: var(--wedding-light); color: var(--wedding-dark); }
  .card--corporate .name-pill { background: var(--corporate-pill); color: #ffffff; }

  .contacts {
    position: absolute;
    left: 306px;
    top: 207px;
    list-style: none;
    font-family: "Didact Gothic", Arial, sans-serif;
    font-size: 15px;
    color: var(--contact-ink);
  }
  .contacts__item { display: flex; align-items: center; height: 36px; white-space: nowrap; }
  .contacts__icon { width: 22px; height: 22px; margin-right: 16px; flex: none; }
</style>
</head>
<body>
  <p class="set-label set-label--wedding">wedding video</p>
  <p class="set-label set-label--corporate">corporate video</p>

  <section class="card card--wedding">
    <div class="card__band card__band--dark"></div>
    <div class="card__band card__band--light"></div>
    <h1 class="brand"><span class="brand__main">lumora</span><span class="brand__sub">STUDIO</span></h1>
    <p class="name-pill">Marisa Hale-Ortega</p>
    <ul class="contacts">
      <li class="contacts__item">
        <svg class="contacts__icon" viewBox="0 0 22 22"><rect width="22" height="22" rx="3" fill="#141414"/><path d="M7 5c-1 0-2 1-1.5 3 1 3.5 3.5 6.5 7 8 1.6.6 3-.2 3-1.2l-2.5-2-1.3 1c-1.6-.8-3-2.4-3.6-4l1.1-1.2L7 5z" fill="#fff"/></svg>
        482-915-3076
      </li>
      <li class="contacts__item">
        <svg class="contacts__icon" viewBox="0 0 22 22"><rect width="22" height="22" rx="3" fill="#141414"/><rect x="4" y="6" width="14" height="10" fill="none" stroke="#fff" stroke-width="1.5"/><path d="M4 6l7 6 7-6" fill="none" stroke="#fff" stroke-width="1.5"/></svg>
        sales@lumorastudio.com.au
      </li>
      <li class="contacts__item">
        <svg class="contacts__icon" viewBox="0 0 22 22"><rect width="22" height="22" rx="3" fill="#141414"/><rect x="4" y="5" width="14" height="9" fill="#fff"/><rect x="8" y="15" width="6" height="2" fill="#fff"/></svg>
        www.lumorastudio.com.au
      </li>
    </ul>
  </section>

  <section class="card card--corporate">
    <div class="card__band card__band--gradient"></div>
    <h2 class="brand"><span class="brand__main">lumora</span><span class="brand__sub">STUDIO</span></h2>
    <p class="name-pill">Marisa Hale-Ortega</p>
    <ul class="contacts">
      <li class="contacts__item">
        <svg class="contacts__icon" viewBox="0 0 22 22"><rect width="22" height="22" rx="3" fill="#141414"/><path d="M7 5c-1 0-2 1-1.5 3 1 3.5 3.5 6.5 7 8 1.6.6 3-.2 3-1.2l-2.5-2-1.3 1c-1.6-.8-3-2.4-3.6-4l1.1-1.2L7 5z" fill="#fff"/></svg>
        482-915-3076
      </li>
      <li class="contacts__item">
        <svg class="contacts__icon" viewBox="0 0 22 22"><rect width="22" height="22" rx="3" fill="#141414"/><rect x="4" y="6" width="14" height="10" fill="none" stroke="#fff" stroke-width="1.5"/><path d="M4 6l7 6 7-6" fill="none" stroke="#fff" stroke-width="1.5"/></svg>
        sales@lumorastudio.net.au
      </li>
      <li class="contacts__item">
        <svg class="contacts__icon" viewBox="0 0 22 22"><rect width="22" height="22" rx="3" fill="#141414"/><rect x="4" y="5" width="14" height="9" fill="#fff"/><rect x="8" y="15" width="6" height="2" fill="#fff"/></svg>
        www.lumorastudio.net.au
      </li>
    </ul>
  </section>
</body>
</html>
```